KLD Forearm Tattoo Enhancement

I have a small tattoo on my forearm. I'd like to add to and expand it, and have it fit roughly on the inside of my forearm. I have additional words/text that I'd like to add to it and other words that could be added or used as concepts in the design. I'm open to the idea of a cool looking word cloud, but that's as creative as I can be. This is a tattoo of my daughters. The current mrtw represents Mara, Rosalind, Tess, Winnie. Existing tattoo must be part of the design. Measurements on the attached image are in mm. Any proposed design should be NOT feminine, floral, or cuddly. Would like design to have a clean look that will last and look good over time. Single color, *maybe* some shading would be ok. There are birth dates associated with each name, but the dates don't necessarily have to be associated with the names in the design. Words/Text to include: Mara Rosalind Tessaly Winifred 5-31-78 8-23-81 12-14-02 9-9-04 Words or concepts to include: Daughters Love Family Sisters Heart Cherish
Other font styles liked:
- match current
Colors
Designer to choose only greyscale colors for use in the design.

```html
<!DOCTYPE html>
<html lang="en">
<head>
<meta charset="utf-8">
<title>KLD Forearm Tattoo Concepts</title>
<link rel="stylesheet" href="https://fonts.googleapis.com/css2?family=Courier+Prime:ital,wght@0,700;1,700&family=Archivo:wght@800&display=swap">
<style>
  :root {
    --canvas: #e2e2e2;
    --divider: #ffffff;
    --ink: #262626;
    --label: #000000;
  }
  html, body {
    margin: 0;
    padding: 0;
    width: 1144px;
    height: 1200px;
    overflow: hidden;
    background: var(--canvas);
  }
  .concept-sheet { display: block; width: 1144px; height: 1200px; }
  .panel-bg { fill: var(--canvas); }
  .divider { fill: var(--divider); }
  .concept-label { font-family: "Archivo", Arial, sans-serif; font-weight: 800; fill: var(--label); }
  .word { font-family: "Courier Prime", "Courier New", monospace; font-weight: 700; fill: var(--ink); }
  .date { font-family: "Courier Prime", "Courier New", monospace; font-style: italic; font-weight: 700; fill: var(--ink); }
  .monogram { font-family: "Courier Prime", "Courier New", monospace; font-weight: 700; fill: var(--ink); }
</style>
</head>
<body>
<svg class="concept-sheet" viewBox="0 0 1000 1049" xmlns="http://www.w3.org/2000/svg" aria-label="Two word cloud tattoo layout concepts">
  <rect class="panel-bg" x="0" y="0" width="1000" height="522"/>
  <rect class="divider" x="0" y="522" width="1000" height="10"/>
  <rect class="panel-bg" x="0" y="532" width="1000" height="517"/>

  <!-- Concept 1 -->
  <g class="concept concept-one">
    <text class="concept-label" x="14" y="92" font-size="84">1</text>
    <g transform="rotate(-3 480 280)">
      <text class="date" x="225" y="172" font-size="30">12.14.02</text>
      <text class="word" x="298" y="218" font-size="48">tessaly</text>
      <text class="word" x="522" y="248" font-size="46">mara</text>
      <text class="date" x="680" y="248" font-size="22">05.31.78</text>
      <text class="word" x="418" y="256" font-size="28">Love</text>
      <text class="word" x="727" y="281" font-size="26">Family</text>
      <text class="monogram" x="248" y="298" font-size="44">mrtw</text>
      <text class="word" x="380" y="296" font-size="40">winifred</text>
      <text class="date" x="520" y="328" font-size="32">09.09.04</text>
      <text class="date" x="92" y="305" font-size="24">08.23.81</text>
      <text class="word" x="100" y="375" font-size="62">rosalind</text>
    </g>
  </g>

  <!-- Concept 2 -->
  <g class="concept concept-two">
    <text class="concept-label" x="14" y="632" font-size="84">2</text>
    <g transform="rotate(-2 480 800)">
      <text class="date" x="205" y="697" font-size="32">12.14.02</text>
      <text class="word" x="278" y="745" font-size="48">tessaly</text>
      <text class="word" x="418" y="786" font-size="34">Love</text>
      <text class="word" x="550" y="788" font-size="64">mara</text>
      <text class="date" x="762" y="770" font-size="24">05.31.78</text>
      <text class="word" x="628" y="806" font-size="24">Family</text>
      <text class="monogram" x="252" y="822" font-size="44">mrtw</text>
      <text class="word" x="405" y="840" font-size="40">winifred</text>
      <text class="date" x="545" y="882" font-size="32">09.09.04</text>
      <text class="word" x="100" y="905" font-size="62">rosalind</text>
      <text class="date" x="320" y="942" font-size="24">08.23.81</text>
    </g>
  </g>
</svg>
</body>
</html>
```